Online Marketplace Startup for Community Facilities (Vondaloft)

A innovative, modern website design is required for a new startup called Vondaloft. Vondaloft will be an online marketplace for searching for and booking community facilities, such as schools facilities (sports grounds, halls, classrooms etc.), churches, hospitals and other community facilities.

The attached brief has been created to provide guidance on the structure and content required.

The web design shall feature a modern, innovative but user friendly interface similar style to other web start up pages:
www.hirewendle.co.uk
www.trundlo.com.au
www.markplinth.com.au

The web design shall be ‘wordpress’ compliant and allow for future functionality to be added and coded (e.g. animations, flash, blogs etc) and content to be editable.

The following brief has been created to provide guidance on the structure and content required.

An existing logo developed for Vondaloft shall be utilised and incorporated in the top left hand cover of the cover landing page (refer to attached logo designs).

Refer to attached 'Website brief' for more details on requirements.
Updates

Project Deadline Extended
Reason: I wish to grant an extension to the deadline to provide designers with more time to submit their designs.

Target Market(s)

VondaLoft will focus on building a customer network of both community facility owners (schools, hospitals, churches) and hirers (non-government organisations, community groups, event management companies, commercial businesses). Members of the general public will also be encouraged to book facilities for private functions.

Industry/Entity Type

Community

Coding

Coded - Design and coding required

Number of Pages Required

5+ page

Font styles to use
Sans Serif

Colors
3176b5
ffffff
85cae6
33a6d7

Requirements
Must have
• The web design shall feature a modern, innovative but user friendly interface similar style to other web start up pages:
• www.hirewendle.co.uk
• www.trundlo.com.au
• www.markplinth.com.au
• The web design shall be ‘wordpress’ compliant and allow for future functionality to be added and coded (e.g. animations, flash, blogs etc) and content to be editable.
• Refer to Project brief for other requirements
Nice to have
• Refer to Project brief
Should not have
• Refer to Project brief

```html
<!DOCTYPE html>
<html lang="en">
<head>
<meta charset="utf-8">
<title>VondaLoft – Community Facility Bookings</title>
<link href="https://fonts.googleapis.com/css2?family=Raleway:wght@400;500;600&family=Open+Sans:wght@400;600&display=swap" rel="stylesheet">
<style>
:root{
  --brand:#3176b5;
  --brand-deep:#1c4c90;
  --hero-dark:#17427f;
  --sky:#33a6d7;
  --sky-soft:#85cae6;
  --white:#ffffff;
  --ink:#1e3f73;
  --text:#555b63;
  --field-line:#d6d8db;
  --panel:#f2f2f3;
  --footer:#3c3c3e;
  --footer-text:#d9d9d9;
}
*{margin:0;padding:0;box-sizing:border-box}
html,body{width:679px;height:1200px;overflow:hidden;background:var(--white)}
body{position:relative;font-family:"Open Sans",Arial,sans-serif;color:var(--text)}
.abs{position:absolute}

/* top strip */
.top-strip{left:0;top:0;width:679px;height:25px;background:var(--brand)}
.social{display:flex;gap:4px}
.social span{width:14px;height:14px;border-radius:50%;background:var(--white);display:block}
.top-strip .social{position:absolute;right:95px;top:6px}

/* header */
.site-header{left:0;top:25px;width:679px;height:47px;background:var(--white);box-shadow:0 1px 2px rgba(0,0,0,.08)}
.brand{display:flex;align-items:center;gap:6px;font-family:"Raleway",Arial,sans-serif;font-weight:500}
.brand-mark{width:14px;height:14px;background:var(--brand-deep)}
.site-header .brand{position:absolute;left:91px;top:14px;font-size:19px;color:var(--brand-deep)}
.main-nav{position:absolute;left:247px;top:20px;display:flex;gap:11px;font-size:7.2px;color:#333}
.main-nav .current{color:var(--brand)}

/* hero */
.hero{left:0;top:72px;width:679px;height:286px;background:linear-gradient(120deg,#1f58a0 0%,var(--hero-dark) 60%,#153a72 100%)}
.hero-title{position:absolute;left:91px;top:76px;font-family:"Raleway",Arial,sans-serif;font-weight:500;font-size:27px;color:var(--white)}
.hero-copy{position:absolute;left:91px;top:117px;width:220px;font-family:"Raleway",Arial,sans-serif;font-size:10.6px;line-height:16px;color:var(--white)}
.btn-outline-light{position:absolute;left:92px;top:175px;width:88px;height:28px;border:2px solid var(--white);color:var(--white);font-family:"Raleway",Arial,sans-serif;font-weight:600;font-size:10px;display:flex;align-items:center;justify-content:center}
.hero-art{position:absolute;left:370px;top:38px;width:220px;height:248px;border-radius:6px;background:radial-gradient(circle at 50% 45%,#f3f3f3 0 18%,#3a79c0 19%,#1d4f92 60%,transparent 75%)}
.slider-dots{position:absolute;left:319px;top:260px;display:flex;gap:3px}
.slider-dots span{width:8px;height:8px;border-radius:50%;background:var(--white)}
.slider-dots .active{background:transparent;border:1.5px solid var(--white)}

/* about */
.about{left:0;top:358px;width:679px;height:253px;background:var(--white)}
.about h2{position:absolute;left:91px;top:43px;font-family:"Raleway",Arial,sans-serif;font-weight:500;font-size:18px;color:var(--ink)}
.about p{position:absolute;left:92px;width:232px;font-size:7.4px;line-height:13.6px;color:var(--text)}
.about .p1{top:76px}
.about .p2{top:110px}
.btn-outline{position:absolute;left:93px;top:167px;width:81px;height:20px;border:1.5px solid var(--brand);color:var(--brand);font-family:"Raleway",Arial,sans-serif;font-size:8.5px;display:flex;align-items:center;justify-content:center}
.about-art{position:absolute;left:340px;top:12px;width:270px;height:204px;background:radial-gradient(ellipse at 50% 50%,#dbe8f4 0 40%,#f4f8fc 70%,var(--white) 100%)}

/* services */
.services{left:0;top:611px;width:679px;height:221px;background:linear-gradient(90deg,var(--brand) 0%,var(--sky) 100%)}
.section-badge{left:331px;top:594px;width:26px;height:26px;background:var(--white);transform:rotate(45deg);box-shadow:0 1px 2px rgba(0,0,0,.1)}
.services h2{position:absolute;left:0;width:679px;top:27px;text-align:center;font-family:"Raleway",Arial,sans-serif;font-weight:500;font-size:18px;color:var(--white)}
.service{position:absolute;top:73px;width:130px;text-align:center}
.service svg{display:block;margin:0 auto}
.service p{margin-top:4px;font-family:"Raleway",Arial,sans-serif;font-size:9.2px;line-height:14px;color:var(--white)}
.service.first p{margin-top:8px}
.arrow{position:absolute;top:97px}

/* enquiry */
.enquiry{left:0;top:832px;width:679px;height:201px;background:linear-gradient(160deg,#e9e9ea 0%,var(--panel) 40%,var(--panel) 100%)}
.enquiry h2{position:absolute;left:0;width:679px;top:19px;text-align:center;font-family:"Raleway",Arial,sans-serif;font-weight:500;font-size:15px;color:var(--ink)}
.enquiry .lead{position:absolute;left:0;width:679px;top:41px;text-align:center;font-family:"Raleway",Arial,sans-serif;font-size:9.5px;color:#333}
.field{position:absolute;left:162px;width:177px;height:20px;background:var(--white);border:1px solid var(--field-line);font-size:6.4px;color:#444;padding:6px 0 0 5px}
.field.select::after{content:"";position:absolute;right:0;top:0;width:15px;height:18px;background:#e4e5e6}
.field.select::before{content:"";position:absolute;right:5px;top:8px;border:2.5px solid transparent;border-top:3px solid #555;z-index:1}
.comments{position:absolute;left:345px;top:67px;width:177px;height:88px;background:var(--white);border:1px solid var(--field-line);font-size:6.4px;color:#444;padding:6px 0 0 5px}
.btn-submit{position:absolute;left:162px;top:161px;width:66px;height:21px;background:var(--sky);color:var(--white);font-family:"Raleway",Arial,sans-serif;font-weight:600;font-size:7.5px;letter-spacing:.5px;display:flex;align-items:center;justify-content:center}

/* footer */
.site-footer{left:0;top:1033px;width:679px;height:167px;background:var(--footer);color:var(--footer-text)}
.site-footer .brand{position:absolute;left:92px;top:22px;font-size:16px;color:var(--white)}
.site-footer .brand-mark{background:var(--white);width:12px;height:12px}
.footer-about{position:absolute;left:92px;top:61px;width:140px;font-size:6.3px;line-height:12.4px}
.footer-col h3{font-family:"Raleway",Arial,sans-serif;font-weight:500;font-size:8.6px;color:var(--white);margin-bottom:10px}
.footer-col{position:absolute;top:23px;font-size:6.2px;line-height:10.6px}
.links{left:258px}
.contact{left:355px}
.contact li{display:flex;gap:5px;line-height:12.7px}
.contact svg{flex:none;margin-top:3px}
.follow{left:521px}
.follow .social span{width:14px;height:14px}
.follow .social span:nth-child(1){background:#3b5ea8}
.follow .social span:nth-child(2){background:#2d9ee0}
.follow .social span:nth-child(3){background:#d9443a}
.follow .social span:nth-child(4){background:#1f70a8}
ul{list-style:none}
.footer-rule{position:absolute;left:92px;top:128px;width:496px;height:1px;background:#5a5a5c}
.copyright{position:absolute;left:0;width:679px;top:140px;text-align:center;font-size:6.2px}
</style>
</head>
<body>

<div class="abs top-strip">
  <div class="social" aria-label="Social links"><span></span><span></span><span></span><span></span></div>
</div>

<header class="abs site-header">
  <div class="brand"><span class="brand-mark"></span>VondaLoft</div>
  <nav class="main-nav">
    <span class="current">Home</span><span>About Us</span><span>How it Works</span><span>Services</span><span>Packages</span><span>Why Us?</span><span>News</span><span>FAQ</span><span>Contact Us</span>
  </nav>
</header>

<section class="abs hero">
  <h1 class="hero-title">VondaLoft</h1>
  <p class="hero-copy">Lorem ipsum dolor sit amet, consectetur ipiscing elit, sed do eiusmod tempor incidi dunt ut labore et dolore magndolo.</p>
  <span class="btn-outline-light">READ MORE</span>
  <div class="hero-art" role="img" aria-label="Illustration of hands holding a tablet showing charts, surrounded by business icons"></div>
  <div class="slider-dots"><span></span><span></span><span class="active"></span><span></span></div>
</section>

<section class="abs about">
  <h2>About VondaLoft</h2>
  <p class="p1">Pellentesque faucibus Ut accumsan ultricies elit Maecenas at justo id velit placerat molestie Donec dictum lectus non odio</p>
  <p class="p2">nec euismod sit amet egestas placerat est Pellentesque habitant morbi tristique senectus et netus et malesuada fames ac turpis egestas Cras id elit Integer quis urna Ut ante</p>
  <span class="btn-outline">Read More</span>
  <div class="about-art" role="img" aria-label="Line-art network of business and technology icons connected by circuit lines"></div>
</section>

<section class="abs services">
  <h2>Our Services</h2>
  <svg class="arrow" style="left:68px" width="14" height="22" viewBox="0 0 14 22"><path d="M11 2 3 11l8 9" fill="none" stroke="#cfe6f5" stroke-width="2"/></svg>
  <svg class="arrow" style="left:600px" width="14" height="22" viewBox="0 0 14 22"><path d="M3 2l8 9-8 9" fill="none" stroke="#cfe6f5" stroke-width="2"/></svg>

  <div class="service first" style="left:80px">
    <svg width="86" height="86" viewBox="0 0 86 86"><rect x="18" y="18" width="50" height="50" transform="rotate(45 43 43)" fill="#1c4c90"/>
      <g fill="none" stroke="#fff" stroke-width="1.6"><path d="M30 38h8l14-8v26l-14-8h-8z"/><path d="M33 48l3 9h4l-2-9"/><path d="M57 36l4-3M58 43h5M57 50l4 3"/></g></svg>
    <p>Marketing and<br>Promotion of your facility</p>
  </div>
  <div class="service" style="left:213px">
    <svg width="86" height="80" viewBox="0 0 86 80"><rect x="18" y="15" width="50" height="50" transform="rotate(45 43 40)" fill="#1c4c90"/>
      <g fill="none" stroke="#fff" stroke-width="1.6"><rect x="28" y="30" width="28" height="19"/><path d="M42 49v6M35 55h14"/><rect x="46" y="24" width="14" height="9" fill="#1c4c90"/></g>
      <g fill="#fff"><circle cx="34" cy="40" r="1.3"/><circle cx="38" cy="40" r="1.3"/><circle cx="42" cy="40" r="1.3"/></g></svg>
    <p>Administer Bookings<br>and Enquiries</p>
  </div>
  <div class="service" style="left:344px">
    <svg width="86" height="80" viewBox="0 0 86 80"><rect x="18" y="15" width="50" height="50" transform="rotate(45 43 40)" fill="#1c4c90"/>
      <g fill="none" stroke="#fff" stroke-width="1.6"><path d="M34 24h18v30l-3-2-3 2-3-2-3 2-3-2-3 2z"/><path d="M38 31h10M38 36h10M38 41h10M38 46h7"/></g></svg>
    <p>Invoicing and<br>Payment collection</p>
  </div>
  <div class="service" style="left:475px">
    <svg width="86" height="80" viewBox="0 0 86 80"><rect x="18" y="15" width="50" height="50" transform="rotate(45 43 40)" fill="#1c4c90"/>
      <g fill="none" stroke="#fff" stroke-width="1.6"><rect x="27" y="27" width="32" height="20"/><path d="M43 47v7M36 54h14"/><path d="M31 43l7-6 6 3 10-8"/></g></svg>
    <p>Bookings Reports<br>and Customer Service</p>
  </div>
</section>
<div class="abs section-badge"></div>

<section class="abs enquiry">
  <h2>Enquiry Form</h2>
  <p class="lead">Lorem ipsum dolor sit amet, consectetur adipiscing</p>
  <div class="field" style="top:67px">Name:</div>
  <div class="field" style="top:90px">School:</div>
  <div class="field" style="top:113px">Email:</div>
  <div class="field select" style="top:136px">Please Select:</div>
  <div class="comments">Comments:</div>
  <span class="btn-submit">SUBMIT</span>
</section>

<footer class="abs site-footer">
  <div class="brand"><span class="brand-mark"></span>VondaLoft</div>
  <p class="footer-about">Lorem ipsum dolor sit amet, consectetur adi ising elit,sed do eiusmod tempor incididunt ut labore et dolore magndolore magna.</p>

  <div class="footer-col links">
    <h3>Links</h3>
    <ul><li>Home</li><li>About us</li><li>How it works</li><li>Services</li><li>Why use us</li><li>FAQ</li></ul>
  </div>

  <div class="footer-col contact">
    <h3>Contact</h3>
    <ul>
      <li><svg width="5" height="7" viewBox="0 0 5 7"><path d="M2.5 0A2.5 2.5 0 0 0 0 2.5C0 4.3 2.5 7 2.5 7S5 4.3 5 2.5A2.5 2.5 0 0 0 2.5 0z" fill="#ddd"/></svg><span>Address: Lorem ipsolorsit,<br>dummy location 584, Location<br>Dummy lorem ispsum.</span></li>
      <li><svg width="6" height="6" viewBox="0 0 6 6"><path d="M1 0l1.3 1.5-.6 1a3 3 0 0 0 1.8 1.8l1-.6L6 5 5 6C2 6 0 4 0 1z" fill="#ddd"/></svg><span>Phone: 878-555-0142</span></li>
      <li><svg width="6" height="5" viewBox="0 0 6 5"><rect width="6" height="5" fill="#ddd"/><path d="M0 0l3 2.5L6 0" fill="none" stroke="#3c3c3e" stroke-width=".7"/></svg><span>Email:info@vondaloft-mail.com</span></li>
    </ul>
  </div>

  <div class="footer-col follow">
    <h3>Follow Us</h3>
    <div class="social"><span></span><span></span><span></span><span></span></div>
  </div>

  <div class="footer-rule"></div>
  <p class="copyright">©2017 Vondaloft All Rights Reserved | Legal and Privacy Statement. Site Map</p>
</footer>

</body>
</html>
```